Business card design only (Have Logo Online) Shoudl be quick and easy for designer

We would like to have a business card design that is in-line with our company logo. Final deliverables should include two EPS extension file. One for the front card design and the other the back-end design. Please also indicate the font style used.

Advisory Pebbles is a social enterprise that focuses on utilizing technology, unique methodologies and international partnerships to provide a one-stop location for economical and dependable IT-related solutions.

Target Market(s)

Micro, small and medium business owners.

Industry/Entity Type

Business

Requirements
Must have
• The business card should incorporate our company logo.
Nice to have
• A little web 2.0 style would be nice but I haven''t decided yet.

```html
<!DOCTYPE html>
<html lang="en">
<head>
<meta charset="utf-8">
<title>Advisory Pebbles — Business Card</title>
<link rel="stylesheet" href="https://fonts.googleapis.com/css2?family=Oswald:wght@500;600&display=swap">
<style>
  :root {
    --backdrop: #ececec;
    --card: #ffffff;
    --green-deep: #2f6b3c;
    --green-brand: #4f8f5b;
    --green-pale: #eaf6e6;
    --green-mid: #9fd69a;
    --green-bright: #3da53a;
    --ink: #111111;
  }
  html, body {
    margin: 0;
    width: 1200px;
    height: 1200px;
    overflow: hidden;
    background: var(--backdrop);
  }
  .canvas {
    position: relative;
    width: 1200px;
    height: 1200px;
    font-family: "Oswald", "Arial Narrow", sans-serif;
  }
  .card {
    position: absolute;
    left: 150px;
    width: 900px;
    height: 540px;
    background: var(--card);
    overflow: hidden;
    box-shadow: 0 2px 10px rgba(0,0,0,0.12);
  }
  .card--front { top: 40px; }
  .card--back { top: 620px; }
  .card__swoosh {
    position: absolute;
    inset: 0;
    width: 900px;
    height: 540px;
  }
  .brand {
    position: absolute;
    display: flex;
    align-items: center;
    margin: 0;
  }
  .brand__mark {
    flex: none;
    background: var(--green-deep);
  }
  .brand__name {
    margin: 0;
    color: var(--green-deep);
    font-weight: 600;
    text-transform: uppercase;
    white-space: nowrap;
    line-height: 1;
  }
  .card--front .brand { left: 130px; top: 238px; gap: 22px; }
  .card--front .brand__mark { width: 48px; height: 48px; }
  .card--front .brand__name { font-size: 64px; letter-spacing: 4px; }
  .card--back .brand { left: 68px; top: 96px; gap: 12px; }
  .card--back .brand__mark { width: 22px; height: 22px; }
  .card--back .brand__name { font-size: 28px; letter-spacing: 1.5px; }
  .contact {
    position: absolute;
    left: 68px;
    top: 190px;
    margin: 0;
    font-style: normal;
    color: var(--ink);
  }
  .contact__name {
    margin: 0;
    font-size: 104px;
    line-height: 1;
    font-weight: 600;
    color: var(--green-brand);
    text-transform: uppercase;
    letter-spacing: -1px;
  }
  .contact__role {
    margin: 2px 0 6px;
    font-size: 34px;
    line-height: 1;
    font-weight: 600;
    letter-spacing: 22px;
    text-transform: uppercase;
  }
  .contact__line {
    margin: 0;
    font-size: 30px;
    line-height: 36px;
    font-weight: 600;
  }
  .contact__line--caps { text-transform: uppercase; }
  .contact__line--email { text-transform: uppercase; letter-spacing: 5px; font-size: 27px; }
</style>
</head>
<body>
<main class="canvas">

  <section class="card card--front" aria-label="Card front">
    <svg class="card__swoosh" viewBox="0 0 900 540" role="img" aria-label="Layered green abstract ribbon pattern sweeping down the right edge">
      <defs>
        <linearGradient id="swoosh-fill" x1="0" y1="0" x2="1" y2="0.35">
          <stop offset="0" stop-color="#eaf6e6"/>
          <stop offset="0.55" stop-color="#a9dca3"/>
          <stop offset="1" stop-color="#3da53a"/>
        </linearGradient>
      </defs>
      <path d="M370,0 Q760,110 850,540 L900,540 L900,0 Z" fill="url(#swoosh-fill)"/>
      <path d="M560,0 Q830,140 885,540 L900,540 L900,0 Z" fill="#6fc16a" opacity="0.45"/>
    </svg>
    <div class="brand">
      <span class="brand__mark" aria-hidden="true"></span>
      <h1 class="brand__name">Advisory Pebbles</h1>
    </div>
  </section>

  <section class="card card--back" aria-label="Card back">
    <svg class="card__swoosh" viewBox="0 0 900 540" role="img" aria-label="Layered green abstract ribbon pattern sweeping down the right edge">
      <defs>
        <linearGradient id="swoosh-fill-back" x1="0" y1="0" x2="1" y2="0.35">
          <stop offset="0" stop-color="#eaf6e6"/>
          <stop offset="0.55" stop-color="#a9dca3"/>
          <stop offset="1" stop-color="#3da53a"/>
        </linearGradient>
      </defs>
      <path d="M370,0 Q760,110 850,540 L900,540 L900,0 Z" fill="url(#swoosh-fill-back)"/>
      <path d="M560,0 Q830,140 885,540 L900,540 L900,0 Z" fill="#6fc16a" opacity="0.45"/>
    </svg>
    <div class="brand">
      <span class="brand__mark" aria-hidden="true"></span>
      <p class="brand__name">Advisory Pebbles</p>
    </div>
    <address class="contact">
      <h2 class="contact__name">Orin Talbeck</h2>
      <p class="contact__role">Founder</p>
      <p class="contact__line">2140 Alder Lane, BC Canada, V3K 2J7</p>
      <p class="contact__line contact__line--caps">www.advisorypebbles.com</p>
      <p class="contact__line">1-555-014-3829</p>
      <p class="contact__line contact__line--email">orin.talbeck@advisorypebbles.com</p>
    </address>
  </section>

</main>
</body>
</html>
```